One label design for 3 different sizes of honey bottles

Our honey company -- Amber Hollow Apiary -- needs new product labels, integrating our new name and logo. We would like one label design that presents equally well on three different sizes of plastic honey bottles. Designs should include a front and back label.

Keep in mind that we really like our old label. Please submit designs that have a similar color and font scheme as the old label.

In the uploaded files, you will find (1) detailed content instructions for each size label (2 lb, 1 lb, 8 oz), (2) photo of three plastic bottles without labels, (3) *.ai file for the new company logo, and (4) image of old package label.

Requirements
Must have
• Same look and feel as our old label, but with our new name and logo

```html
<!DOCTYPE html>
<html lang="en">
<head>
<meta charset="utf-8">
<title>Amber Hollow Apiary – Honeycomb Label, Front and Back</title>
<link href="https://fonts.googleapis.com/css2?family=Rye&family=Courier+Prime:wght@400;700&family=Archivo+Narrow:wght@400;700&display=swap" rel="stylesheet">
<style>
  :root {
    --page: #ffffff;
    --label: #f9f0e1;
    --gold: #c9a137;
    --gold-light: #e2c777;
    --comb: #efe3c9;
    --ink: #2e2b27;
    --text: #3a3631;
  }
  * { box-sizing: border-box; margin: 0; padding: 0; }
  html, body { width: 779px; height: 1200px; overflow: hidden; background: var(--page); }
  .sheet { position: relative; width: 779px; height: 1200px; }
  .label {
    position: absolute; top: 294px; width: 355px; height: 612px;
    background: var(--label); overflow: hidden;
    font-family: "Courier Prime", "Courier New", monospace; color: var(--text);
  }
  .label--front { left: 24px; }
  .label--back { left: 400px; }
  .label__frame { position: absolute; inset: 0; }
  .comb-pattern {
    position: absolute; border-radius: 6px;
    background: var(--comb);
  }
  .tagline {
    position: absolute; top: 42px; width: 100%; text-align: center;
    font-size: 13px; letter-spacing: .5px; color: var(--text);
  }
  .product-name {
    position: absolute; top: 88px; width: 100%; text-align: center;
    font-family: "Rye", Georgia, serif; font-size: 35px; font-weight: 400; color: var(--ink); letter-spacing: 0;
  }
  .ornament {
    position: absolute;
    background: linear-gradient(180deg, var(--gold-light), var(--gold));
    opacity: .55; border-radius: 40%;
  }
  .ornament--swirl { left: 75px; top: 142px; width: 205px; height: 12px; }
  .ornament--bee { left: 34px; top: 432px; width: 287px; height: 146px; opacity: .35; border-radius: 30% 30% 10% 10%; }
  .brand-name {
    position: absolute; top: 255px; width: 100%; text-align: center;
    font-size: 27px; font-weight: 700; line-height: 1.15; color: var(--gold);
  }
  .net-weight {
    position: absolute; left: 44px; top: 390px; width: 267px; height: 30px;
    border: 1.5px solid var(--ink); text-align: center; line-height: 27px;
    font-size: 14px; letter-spacing: .8px; color: var(--ink);
  }
  .promise {
    position: absolute; left: 38px; top: 100px; width: 279px; text-align: center;
    font-size: 13px; line-height: 17px; color: var(--ink);
  }
  .nutrition {
    position: absolute; left: 45px; top: 372px; width: 266px; height: 59px;
    border: 1.2px solid var(--ink); padding: 3px 5px; background: var(--label);
    font-family: "Archivo Narrow", Arial, sans-serif; font-size: 5.6px; line-height: 7px; color: var(--ink);
  }
  .nutrition__title { font-size: 10px; font-weight: 700; }
  .nutrition b { font-weight: 700; }
  .nutrition__note { font-size: 4.4px; line-height: 6px; }
  .back-footer { position: absolute; left: 48px; top: 464px; width: 270px; height: 60px; }
  .warning { position: absolute; left: 0; top: 4px; width: 120px; font-size: 7.5px; line-height: 10px; }
  .divider { position: absolute; left: 130px; top: 0; width: 1px; height: 60px; background: var(--gold); }
  .contact { position: absolute; left: 151px; top: 2px; font-size: 7.5px; line-height: 10.5px; font-style: normal; }
</style>
</head>
<body>
<main class="sheet">

  <section class="label label--front" aria-label="Front label">
    <div class="comb-pattern" style="left:180px;top:165px;width:146px;height:205px;" role="img" aria-label="Faint honeycomb pattern"></div>
    <div class="comb-pattern" style="left:29px;top:440px;width:297px;height:140px;" role="img" aria-label="Faint honeycomb pattern"></div>
    <svg class="label__frame" viewBox="0 0 355 612" aria-hidden="true">
      <path d="M40 22 H315 A22 22 0 0 0 337 44 V88 H332 V524 H337 V568 A22 22 0 0 0 315 590 H40 A22 22 0 0 0 18 568 V524 H23 V88 H18 V44 A22 22 0 0 0 40 22 Z" fill="none" stroke="var(--gold)" stroke-width="3"/>
      <path d="M44 28 H311 A20 20 0 0 0 331 48 V84 H326 V528 H331 V564 A20 20 0 0 0 311 584 H44 A20 20 0 0 0 24 564 V528 H29 V84 H24 V48 A20 20 0 0 0 44 28 Z" fill="none" stroke="var(--gold)" stroke-width="1"/>
      <line x1="60" y1="39" x2="295" y2="39" stroke="var(--gold)" stroke-width="1"/>
      <line x1="60" y1="69" x2="295" y2="69" stroke="var(--gold)" stroke-width="1"/>
    </svg>
    <p class="tagline">LOCAL • PURE • RAW</p>
    <h1 class="product-name">HONEYCOMB</h1>
    <div class="ornament ornament--swirl" role="img" aria-label="Gold flourish ornament"></div>
    <p class="brand-name">Amber Hollow<br>Apiary</p>
    <p class="net-weight">Net Wt. 1 LB (454 g)</p>
    <div class="ornament ornament--bee" role="img" aria-label="Engraved honeybee illustration framed by gold scrollwork"></div>
  </section>

  <section class="label label--back" aria-label="Back label">
    <div class="comb-pattern" style="left:190px;top:75px;width:136px;height:225px;" role="img" aria-label="Faint honeycomb pattern"></div>
    <div class="comb-pattern" style="left:29px;top:330px;width:130px;height:100px;" role="img" aria-label="Faint honeycomb pattern"></div>
    <div class="comb-pattern" style="left:150px;top:530px;width:176px;height:50px;" role="img" aria-label="Faint honeycomb pattern"></div>
    <svg class="label__frame" viewBox="0 0 355 612" aria-hidden="true">
      <path d="M40 22 H315 A22 22 0 0 0 337 44 V88 H332 V524 H337 V568 A22 22 0 0 0 315 590 H40 A22 22 0 0 0 18 568 V524 H23 V88 H18 V44 A22 22 0 0 0 40 22 Z" fill="none" stroke="var(--gold)" stroke-width="3"/>
      <path d="M44 28 H311 A20 20 0 0 0 331 48 V84 H326 V528 H331 V564 A20 20 0 0 0 311 584 H44 A20 20 0 0 0 24 564 V528 H29 V84 H24 V48 A20 20 0 0 0 44 28 Z" fill="none" stroke="var(--gold)" stroke-width="1"/>
      <line x1="60" y1="69" x2="295" y2="69" stroke="var(--gold)" stroke-width="1"/>
    </svg>
    <p class="promise">“Amber Hollow Apiary promises 100% pure honey, never pasteurized, and sourced exclusively from beehives we keep near Cedar Run, West Virginia</p>
    <div class="nutrition">
      <p><span class="nutrition__title">Nutrition Facts</span> Servings: 16, <b>Serv. size: 1 Tbsp (21g),</b></p>
      <p>Amount per serving: <b style="font-size:8px">Calories 60</b>, <b>Total Fat</b> 0g (0% DV), Sat. Fat 0g (0% DV),</p>
      <p><i>Trans</i> Fat 0g, <b>Cholest.</b> 0mg (0% DV), <b>Sodium</b> 0mg (0% DV), <b>Total Carb.</b> 17g (6% DV),</p>
      <p>Fiber 0g (0% DV), Total Sugars 17g (Incl. 17g Added Sugars, 34% DV), <b>Protein</b> 0g,</p>
      <p>Vit. D (0% DV), Calcium (0% DV), Iron (0% DV), Potas. (0% DV).</p>
      <p class="nutrition__note">* One serving adds 17g of sugar to your diet and represents 34% of the Daily Value for Added Sugars.</p>
    </div>
    <div class="back-footer">
      <p class="warning">“DO NOT FEED HONEY TO INFANTS UNDER ONE YEAR OLD</p>
      <span class="divider"></span>
      <address class="contact">Amber Hollow Apiary<br>112 Linden Hollow Rd<br>Cedar Run, WV 25000<br>www.amberhollowapiary.co</address>
    </div>
  </section>

</main>
</body>
</html>
```